Marnie Holloway 2014 Calendar

We need a 12 month, wall hanging Calendar design featuring the actress Marnie Holloway. It is a product for her fans and the feel of this years photographs is very otherworldly with saturated colors and the incorporation of elements such as fire, ice and water. We are looking for bold, graphic designs to support and reflect this feel. There is a very tight schedule for the completion of this calendar as it needs to go into production asap so any designers submitting concepts should have the ability and enthusiasm to dedicate the necessary time required to get this product to the printers quickly.
We have included three of the twelve photographs for you to use with a combination of vertical and horizontal images. Once the design is selected we will provide the remaining nine photos to be incorporated. These images are to be kept completely confidential please.
Thank you and we are looking forward to seeing your ideas!!
Industry/Entity Type
Product
Requirements
Must have
- Bio about Marnie Holloway, crédits for art director, photographer etc. Some negative space on cover so that it maybe autographed by actress. 12 months reflected in page design.

```html
<!DOCTYPE html>
<html lang="en">
<head>
<meta charset="utf-8">
<title>Wall Calendar 2014 – January</title>
<link href="https://fonts.googleapis.com/css2?family=Josefin+Sans:wght@300;700&family=Poiret+One&display=swap" rel="stylesheet">
<style>
  :root {
    --photo-deep: #2a0f1e;
    --photo-mid: #6e2140;
    --photo-warm: #b23a4a;
    --photo-pink: #d98aa8;
    --panel-tint: rgba(120, 60, 90, 0.28);
    --ink-light: #f4eef2;
    --ink-rule: rgba(244, 238, 242, 0.75);
    --ink-logo: #3a1a2c;
    --accent-orange: #f08a24;
  }
  html, body {
    margin: 0;
    padding: 0;
    overflow: hidden;
    background: #ffffff;
  }
  .calendar-page {
    position: relative;
    width: 1200px;
    height: 1000px;
    overflow: hidden;
    font-family: "Josefin Sans", sans-serif;
    color: var(--ink-light);
  }
  .cover-photo {
    position: absolute;
    inset: 0;
    background:
      radial-gradient(ellipse 380px 300px at 150px 380px, rgba(240, 120, 70, 0.55), transparent 70%),
      radial-gradient(ellipse 300px 420px at 520px 600px, rgba(60, 120, 70, 0.35), transparent 70%),
      radial-gradient(ellipse 420px 700px at 1080px 520px, rgba(230, 150, 185, 0.75), transparent 75%),
      linear-gradient(100deg, var(--photo-deep) 0%, var(--photo-mid) 35%, var(--photo-warm) 65%, var(--photo-pink) 100%);
  }
  .month-panel {
    position: absolute;
    left: 640px;
    top: 115px;
    width: 560px;
    height: 715px;
    background: var(--panel-tint);
  }
  .brand-name {
    position: absolute;
    left: 765px;
    top: 118px;
    margin: 0;
    font-family: "Poiret One", sans-serif;
    font-size: 84px;
    font-weight: 400;
    line-height: 1;
    color: var(--ink-logo);
    letter-spacing: 1px;
  }
  .month-number {
    position: absolute;
    left: 696px;
    top: 330px;
    font-family: "Poiret One", sans-serif;
    font-size: 84px;
    line-height: 1;
  }
  .month-name {
    position: absolute;
    left: 815px;
    top: 374px;
    font-size: 32px;
    font-weight: 300;
    line-height: 1;
  }
  .year {
    position: absolute;
    left: 965px;
    top: 330px;
    font-family: "Poiret One", sans-serif;
    font-size: 84px;
    line-height: 1;
  }
  .rule-vertical {
    position: absolute;
    left: 790px;
    top: 330px;
    width: 1px;
    height: 442px;
    background: var(--ink-rule);
  }
  .rule-horizontal {
    position: absolute;
    left: 697px;
    top: 422px;
    width: 446px;
    height: 1px;
    background: var(--ink-rule);
  }
  .month-grid {
    position: absolute;
    left: 815px;
    top: 460px;
    width: 348px;
    display: grid;
    grid-template-columns: repeat(7, 49.7px);
    grid-template-rows: 36px repeat(5, 57.5px);
    text-align: center;
    align-items: center;
  }
  .weekday {
    font-size: 26px;
    font-weight: 700;
    line-height: 1;
  }
  .day {
    font-size: 38px;
    font-weight: 300;
    line-height: 1;
    letter-spacing: -1px;
  }
  .day--highlight {
    color: var(--accent-orange);
    font-weight: 700;
  }
  .day--first { grid-column-start: 3; }
</style>
</head>
<body>
  <main class="calendar-page">
    <div class="cover-photo" role="img" aria-label="Night street photograph of a model in a military-style cap and jacket, posing on a coin-operated kiddie motorbike ride under neon pink and red light"></div>

    <div class="month-panel"></div>

    <h1 class="brand-name">LOGO</h1>

    <div class="month-number">01</div>
    <div class="month-name">january</div>
    <div class="year">2014</div>

    <div class="rule-vertical"></div>
    <div class="rule-horizontal"></div>

    <div class="month-grid">
      <span class="weekday">M</span><span class="weekday">T</span><span class="weekday">W</span><span class="weekday">T</span><span class="weekday">F</span><span class="weekday">S</span><span class="weekday">S</span>
      <span class="day day--first day--highlight">1</span><span class="day">2</span><span class="day">3</span><span class="day">4</span><span class="day">5</span>
      <span class="day">6</span><span class="day">7</span><span class="day">8</span><span class="day">9</span><span class="day">10</span><span class="day">11</span><span class="day">12</span>
      <span class="day">13</span><span class="day">14</span><span class="day">15</span><span class="day">16</span><span class="day">17</span><span class="day">18</span><span class="day">19</span>
      <span class="day day--highlight">20</span><span class="day">21</span><span class="day">22</span><span class="day">23</span><span class="day">24</span><span class="day">25</span><span class="day">26</span>
      <span class="day">27</span><span class="day">28</span><span class="day">29</span><span class="day">30</span><span class="day">31</span>
    </div>
  </main>
</body>
</html>
```